Business Card Design Project

We need a business card for our business called Our Harbour Lender. (www.ourharbourlender.com.au)

There are 3 of us in the business, the design we choose will stay the same for all 3 of us, but will need names changed and mobile numbers added. I will provide details in an attachment.

We are a professional services directory for mortgage brokers. I will attach an idea that I had, but happy for you to be free in your designs. We would like the colour scheme to remain within our company colours - blue, white, grey and orange.

Thanks so much for helping us with this project. If you need anymore information, please don't hesitate to ask.

Industry/Entity Type

Business

Requirements
Must have
• Our Harbour Lender Logo
Colour blue and orange to match closely with our logo samples if possible.
The most important card is the card for Tilda Brennan

```html
<!DOCTYPE html>
<html lang="en">
<head>
<meta charset="utf-8">
<title>Our Harbour Lender – Business Cards</title>
<link rel="stylesheet" href="https://fonts.googleapis.com/css2?family=Cabin:wght@400;500;600&display=swap">
<style>
  :root {
    --bg: #e9ebee;
    --blue: #1b9bdb;
    --blue-light: #3fb6ec;
    --blue-deep: #0f88c9;
    --white: #ffffff;
    --ink: #3c3c3c;
    --label: #1b9bdb;
  }
  * { box-sizing: border-box; margin: 0; padding: 0; }
  html, body { width: 1200px; height: 1054px; overflow: hidden; }
  body {
    position: relative;
    background: var(--bg);
    font-family: "Cabin", sans-serif;
    color: var(--ink);
  }
  .card {
    position: absolute;
    width: 528px;
    height: 292px;
    overflow: hidden;
    box-shadow: 0 3px 10px rgba(0,0,0,0.18);
  }
  .card--rounded { border-radius: 26px; }
  .card--front { background: var(--white); }
  .card--back {
    background: radial-gradient(ellipse at 45% 35%, var(--blue-light) 0%, var(--blue) 55%, var(--blue-deep) 100%);
    display: flex; align-items: center; justify-content: center; gap: 16px;
  }
  .pos-a { left: 59px;  top: 59px; }
  .pos-b { left: 614px; top: 152px; }
  .pos-c { left: 59px;  top: 610px; }
  .pos-d { left: 614px; top: 701px; }

  .front__header {
    position: absolute; left: 0; top: 0; width: 100%; height: 66px;
    background: linear-gradient(180deg, var(--blue-light), var(--blue));
    display: flex; align-items: center; justify-content: flex-end; gap: 7px;
    padding-right: 28px;
  }
  .brand-dot {
    width: 18px; height: 18px; border-radius: 50%;
    border: 3px solid var(--white);
  }
  .brand-name {
    color: var(--white); font-weight: 500; font-size: 19px; letter-spacing: -0.2px;
  }
  .front__name {
    position: absolute; left: 27px; top: 108px;
  }
  .person-name {
    color: var(--blue); font-size: 25px; font-weight: 400; line-height: 1; letter-spacing: 0.2px;
  }
  .person-role { font-size: 16px; margin-top: 5px; }
  .front__contact {
    position: absolute; left: 233px; top: 110px; font-size: 15px; line-height: 20px; font-weight: 500;
  }
  .contact-row .label { color: var(--label); display: inline-block; width: 18px; }
  .contact-web { margin-top: 8px; font-size: 14px; }
  .front__footer {
    position: absolute; left: 0; bottom: 0; width: 100%; height: 35px;
    background: linear-gradient(180deg, var(--blue-light), var(--blue));
    color: var(--white); font-size: 12.5px; font-weight: 500;
    display: flex; align-items: center; padding-left: 27px;
  }
  .front__footer .sep { color: #f29a2e; margin: 0 6px; }

  .back__mark {
    width: 58px; height: 58px; border-radius: 50%; border: 7px solid var(--white); flex: none;
  }
  .back__name {
    color: var(--white); font-size: 44px; font-weight: 500; letter-spacing: -0.5px;
  }
</style>
</head>
<body>

<!-- square-corner set -->
<section class="card card--front pos-a" aria-label="Business card front">
  <header class="front__header"><span class="brand-dot"></span><span class="brand-name">Our Harbour Lender</span></header>
  <div class="front__name">
    <p class="person-name">TILDA BRENNAN</p>
    <p class="person-role">CEO/Founder</p>
  </div>
  <div class="front__contact">
    <p class="contact-row"><span class="label">P</span>1300 OURLEND</p>
    <p class="contact-row"><span class="label">M</span>0400 555 218</p>
    <p class="contact-row"><span class="label">F</span>02 5550 1947</p>
    <p class="contact-row"><span class="label">E</span>tilda@ourharbourlender.com</p>
    <p class="contact-web">www.ourharbourlender.com.au</p>
  </div>
  <footer class="front__footer">Our Harbour Lender is a Northpoint Capital Group Pty Ltd project<span class="sep">•</span>ABN 41 202 555 718</footer>
</section>

<section class="card card--back pos-b" aria-label="Business card back">
  <span class="back__mark"></span><span class="back__name">Our Harbour Lender</span>
</section>

<!-- rounded-corner set -->
<section class="card card--front card--rounded pos-c" aria-label="Business card front, rounded">
  <header class="front__header"><span class="brand-dot"></span><span class="brand-name">Our Harbour Lender</span></header>
  <div class="front__name">
    <p class="person-name">TILDA BRENNAN</p>
    <p class="person-role">CEO/Founder</p>
  </div>
  <div class="front__contact">
    <p class="contact-row"><span class="label">P</span>1300 OURLEND</p>
    <p class="contact-row"><span class="label">M</span>0400 555 218</p>
    <p class="contact-row"><span class="label">F</span>02 5550 1947</p>
    <p class="contact-row"><span class="label">E</span>tilda@ourharbourlender.com</p>
    <p class="contact-web">www.ourharbourlender.com.au</p>
  </div>
  <footer class="front__footer">Our Harbour Lender is a Northpoint Capital Group Pty Ltd project<span class="sep">•</span>ABN 41 202 555 718</footer>
</section>

<section class="card card--back card--rounded pos-d" aria-label="Business card back, rounded">
  <span class="back__mark"></span><span class="back__name">Our Harbour Lender</span>
</section>

</body>
</html>
```